strength and conditioning business needs a brochure

We are after a simple yet bold brochure design that uses base colours of red, white, black and grey. We have supporting text that we would like incorporated to see how it all looks as a finished product, as well as the logo.
Reason: To give designers a last chance to make recommended changes before choice is made.

```html
<!DOCTYPE html>
<html lang="en">
<head>
<meta charset="utf-8">
<title>Core Strength Collective – Brochure Inside Spread</title>
<link rel="stylesheet" href="https://fonts.googleapis.com/css2?family=Exo+2:wght@400;500;600&family=Russo+One&display=swap">
<style>
  :root {
    --red: #d01f27;
    --red-dark: #a8151b;
    --black: #141414;
    --charcoal: #262626;
    --graphite: #3a3a3a;
    --light: #efefef;
    --white: #ffffff;
    --ink: #2b2b2b;
    --body: "Exo 2", Arial, sans-serif;
    --display: "Russo One", Impact, sans-serif;
  }
  * { box-sizing: border-box; margin: 0; padding: 0; }
  html, body { width: 1200px; height: 465px; overflow: hidden; background: var(--white); }
  .spread { position: relative; width: 1200px; height: 465px; overflow: hidden; font-family: var(--body); color: var(--ink); background: linear-gradient(180deg, var(--white) 0%, var(--light) 100%); }

  .photo { position: absolute; top: 0; height: 200px; }
  .photo--bench { left: 0; width: 600px; background: linear-gradient(120deg, #1c1c1c 0%, #6b6b6b 45%, #bdbdbd 70%, #3c3c3c 100%); }
  .photo--pulldown { left: 600px; width: 600px; background: linear-gradient(100deg, #0e0e0e 0%, #2e2e2e 35%, #6a6a6a 60%, #1a1a1a 100%); }
  .photo--partners { position: absolute; left: 405px; top: 372px; width: 160px; height: 84px; background: radial-gradient(ellipse at 50% 65%, #3a3a3a 0%, #8a8a8a 50%, rgba(239,239,239,0) 78%); }

  .title-band { position: absolute; left: 0; top: 150px; width: 1200px; height: 52px; }
  .title { position: absolute; top: 156px; left: 372px; width: 660px; white-space: nowrap; font-family: var(--display); font-weight: 400; font-size: 38px; letter-spacing: 1.5px; color: var(--white); -webkit-text-stroke: 1.2px var(--red-dark); line-height: 44px; }
  .title span + span { margin-left: 22px; }

  .intro { position: absolute; left: 10px; top: 209px; width: 592px; font-size: 11px; line-height: 15.5px; letter-spacing: -0.05px; color: var(--ink); }

  .topics { position: absolute; left: 0; top: 252px; width: 300px; height: 205px; }
  .topics__lead { position: absolute; left: 10px; top: 257px; width: 270px; font-size: 11.5px; line-height: 15px; color: var(--white); }
  .topic-list { position: absolute; left: 0; top: 290px; width: 290px; list-style: none; }
  .topic-list li { height: 18px; margin-bottom: 3.6px; padding-left: 10px; font-size: 10px; line-height: 18px; color: var(--white); white-space: nowrap; overflow: hidden; background: var(--red); clip-path: polygon(0 0, 96% 0, 100% 100%, 0 100%); box-shadow: 0 2px 0 var(--graphite); }
  .topic-list small { font-size: 4.4px; margin-left: 3px; vertical-align: middle; }

  .details { position: absolute; left: 307px; top: 244px; width: 288px; font-size: 11px; line-height: 15.6px; color: var(--ink); }
  .details p + p { margin-top: 9px; }

  .reasons-bg { position: absolute; left: 600px; top: 200px; width: 600px; height: 257px; }
  .reason-label { position: absolute; left: 612px; font-family: var(--body); font-weight: 600; font-size: 16px; letter-spacing: .5px; color: var(--white); line-height: 20px; }
  .reason-text { position: absolute; left: 795px; width: 395px; font-size: 8.8px; line-height: 11.5px; color: var(--white); text-align: right; }

  .footer-strip { position: absolute; left: 0; top: 456px; width: 1200px; height: 9px; background: var(--red); }
</style>
</head>
<body>
<main class="spread">
  <div class="photo photo--bench" role="img" aria-label="Black and white photo of a man lifting a barbell on a bench press"></div>
  <div class="photo photo--pulldown" role="img" aria-label="Black and white photo of a woman training on a cable pulldown machine"></div>

  <svg class="title-band" viewBox="0 0 1200 52" aria-hidden="true">
    <polygon points="0,38 340,38 360,10 1060,10 1080,38 1200,38 1200,52 0,52" fill="var(--black)"/>
    <polygon points="0,42 345,42 365,14 1055,14 1075,42 1200,42 1200,46 1072,46 1052,18 368,18 348,46 0,46" fill="var(--red)"/>
    <polygon points="360,10 1060,10 1052,18 368,18" fill="var(--red)"/>
  </svg>
  <h1 class="title"><span>ABOUT US</span><span>WHY CHOOSE CSC?</span></h1>

  <p class="intro">Core Strength Collective (CSC) is an educational resource dedicated to providing coaches, trainers and trainees with the best information available in the areas of strength and body recomposition (muscle gain and fat loss).</p>

  <svg class="topics" viewBox="0 0 300 205" aria-hidden="true">
    <polygon points="0,0 280,0 300,20 300,205 0,205" fill="var(--black)"/>
  </svg>
  <p class="topics__lead">Each month 2-4 in-depth articles are posted from one of the following areas:</p>
  <ul class="topic-list">
    <li>Psychology/Philosophy</li>
    <li>Exercises<small>(in depth analysis of how to perform exercises with videos of athletes performing a work set)</small></li>
    <li>Programming/Training<small>(intensity, volume, frequency, periodization etc.)</small></li>
    <li>Diet</li>
    <li>Recovery<small>(all methods to enhance recovery e.g. foam rolling, sleep etc.)</small></li>
    <li>Product Review<small>(reviews of any products like books that would be useful for coaches/trainers)</small></li>
    <li>Research/Statistics<small>(boring yes but vital if you want to read research and apply it)</small></li>
    <li>Coach/Trainer<small>(issues that specifically face coaches and trainers)</small></li>
  </ul>

  <div class="details">
    <p>In addition to the articles released every month, a discussion forum will be open where any questions and topics can be asked/discussed. It will also be an opportunity for fellow coaches/trainers to network.</p>
    <p>CSC can be purchased as either a monthly subscription ($10 per month) or a yearly one ($100) which gives full access to all content that has been released up until the time of joining.</p>
  </div>
  <div class="photo--partners" role="img" aria-label="Silhouette photo of two people training together with a medicine ball"></div>

  <svg class="reasons-bg" viewBox="0 0 600 257" aria-hidden="true">
    <rect x="0" y="0" width="600" height="257" fill="var(--white)"/>
    <polygon points="0,18 180,18 200,10 600,10 600,257 0,257" fill="var(--charcoal)"/>
    <g fill="var(--black)">
      <polygon points="0,22 190,22 205,50 0,50"/>
      <polygon points="0,58 190,58 205,86 0,86"/>
      <polygon points="0,95 190,95 205,123 0,123"/>
      <polygon points="0,136 190,136 205,164 0,164"/>
      <polygon points="0,180 190,180 205,208 0,208"/>
    </g>
    <g fill="none" stroke="var(--red)" stroke-width="3">
      <polyline points="0,18 180,18 200,10 600,10"/>
      <polyline points="0,52 205,52 225,44 600,44"/>
      <polyline points="0,88 205,88 228,80 600,80"/>
      <polyline points="0,125 205,125 228,117 600,117"/>
      <polyline points="0,166 205,166 228,158 600,158"/>
      <polyline points="0,210 205,210 228,202 600,202"/>
    </g>
  </svg>

  <h2 class="reason-label" style="top:226px">SCIENTIFIC:</h2>
  <h2 class="reason-label" style="top:262px">PRACTICALITY:</h2>
  <h2 class="reason-label" style="top:299px">INTEGRITY:</h2>
  <h2 class="reason-label" style="top:340px">SUPPORT:</h2>
  <h2 class="reason-label" style="top:384px">COST:</h2>

  <p class="reason-text" style="top:254px">Every article that is written takes into account the latest research available in the scientific literature, providing you with the best information that science can currently offer.</p>
  <p class="reason-text" style="top:293px">While scientifically based, every article that is written also relies on observation, personal experiences of others and tacit knowledge (knowledge obtained from doing).</p>
  <p class="reason-text" style="top:328px">CSC prides itself on being an objective source. No affiliations do or will exist with other businesses to remove the possibility of any bias or hidden agendas (which are more common than most think).</p>
  <p class="reason-text" style="top:369px">Whether you are a seasoned trainer, just getting started or simply want to know more about how best to optimise your training, diet and mental approach, support will always be available through the group's forum where questions can be asked and answered.</p>
  <p class="reason-text" style="top:416px">At $10 a month, this is a very cost effective strategy for coaches, trainers and trainees alike to improve their knowledge without breaking the budget. In fact, knowledge gained from CSC will likely SAVE you money in the long term.</p>

  <div class="footer-strip"></div>
</main>
</body>
</html>
```